Your new Home.

below is a lot of info so you can read and understand what I do I think it's important for the creator to know as much as possible so you can creatively decide what would work in a flyer. I want it to be edgy, modern, or very aggressive. I am very loud and proud we don't want to be like everyone else. Our slogan Is "Where Tradesmen Come to Turn Champions" as every one in my business calls themselves professionals and being a master to me means the best at what you do. which we are. my company colors are Gold Maroon Black and grey and whit. I do like having lightning strikes and hail incorperated. We Do Have Promotions and coupons and referals we pay out on. below this is a bunch of info to understand what I do. I need a flyer that is informative about my company. That informs customers what we want to do. We are a company with over 30 years combined experience Myself 13 yrs experience. We are a Storm Damage Specialist Restoration General Contractor Company. We provide a service the helps insure homeowners not only can we provide the correct perferred method of repairs according to today's industry standards rules and regulations. but we know what is your responsibility as a homeowner, and what the responsibility of your insurer is according to The governing municipalities not only by the city and state, but according to States Insurance Departments That govern what Insurance carriers must do. We don't let big conglomerate companies profiting off thousands of homeowners constantly paying in with their raising premiums each year. We use the Guidelines set by the insurance commissioners office to make sure that carriers are approving and paying for more than just minimums. Carriers constantly state to homeowners and contractors that their company policies don't allow things especially when it comes to paying for full roof replacements, replacing all your siding on the entire home if its discontinued. Or replacing all gutters ect. Carriers constantly are coming in only approving and paying for minor repairs And doing partial roof replacements, patching in siding replacing 1 and 2 peices here and their sections of fascia and gutters ect. we are tired of Carriers using their tactics of Denying claims, defering responsibility, defending them self's . Who's left to defend the homeowners? Who's knows the right questions to ask, and in what order and when to ask them. We Do. That's because for over a decade We have perfected the process of Working with hundred of different carriers. By already having major success on over a couple thousand Storm Damage claims . in more than a decade. Every last one of the claims we have worked on. Our goal was to maximize each claim to complete repairs restoring homeowners damaged properties to their original condition as they were prior to their loss. We can't get carriers to do anything they are not obligated to do. We have have to document and and present any and all damages we find. Then present it in a way to a carrier to where it can't be denied stating it doesn't meet certan criteria's, or deferred that its not storm damage that it was caused by a non covered peril, or defend that they are their to take care of you, and we are just trying to make money off of them regardless of actual responsibility. We can navigate through this process where we are the ones taking all the risks and doing all the leg work. Our Time is very valuable. We can only be as effective as our customers allow. Meaning A lot of times carriers will try to divide and conquer. Meaning they want to cause doubt in our abilities, or paint a pictured of alternative Motives That aren't in your best intrest. Carriers know their contracts are with the insured not the Contractors . That they don't have to answer to us
That's why its very important to us to set the tone early on. We are here to make money by performing excellent work restoring your property from storm damage. Ask your self , if we sign homeowners up for us to be the Contractor of choice to repair all approved works, and we only make money off of works completed than wouldn't we want to get you as much work approved for us to do. Leaving the homeowner and the contractor us having the same goal, however carriers dont want that because they are the ones having to pay for it back. They don't want to pay out huge portions they have accumulated from all your yearly premiums. All our works have to be approved by the carriers no carrier is going to pay thousands to their policy holders unless they have to. You are kidding yourself if you don't think they aren't saving millions by not paying out when they are legally bond to. You entered a bi lateral contract with them that you would give them x amount of dollars for a service they would provide if certain listed perils occurred while your insurance was binded / in affect. We know what works and what doesn't. In the end we also don't set the prices we use a 3rd party system that all the carriers use That is a automated computer system that populates the current fair market value of all materials amd labors. Know as the Replacement Cost Value. So if we don't make the rule, or set the prices, and we do all our works upfront with no down payment. Theirs no way a carrier can when a argument that we are doing anything other than working for you to create as much work for us that results in your property Being restored to its original condition at the same time it is restoring thousands of dollars of value back into your. home. Leaving you most prized financial investment protected. Our goals are t ok perform the best quality workmanship and keeping homeowners out of pocket cost to not exceed their set deductibles. If your cost is the same regardless you know when you file a claim you want everything that would be related to storm damaged documented and restored and paid for, and that's what we want because that's what we do for a living, and we want to be the best at it.

explaining the proccess.

We schedual a free no obligation gable crest property damage assesment/ inspection, what that intales is A roof inspection of all roof surfaces on property and a exterior inspection f all structures on the property Dwelling Detacjed Garages Barns, Shops, Well Houses and more. And finally interior inspections as well. Looking for water damage to ceilings and walls and floors.

Once we have photo documented all the damages notated during inspection, a gable crest will then sit down and go over all of them and show you pictures we took of those damages and explain why they we believe they should be paid for by your carrier as a covered peril on you homeowners policy. All with you only paying a
deductible that you chose when you started the policy. We will then use a storm Damage app to populate your best storm Date of Loss That best helps your scenario to get all damages paid for. once we have shown you the damages and explained them to you. we will give you a contingency contract that is based off of us getting your insurance company you approve and pay for them. if we can't get your project approved you don't owe us a dime for all that time we spent inspecting documenting and calling in your claim and meeting your insurance scheduled adjuster. As this is how we make a living is winding homeowners with storm related damage. so once you have decided to see what we can do for you we file your claim with you. Then the adjuster assigned will reach out to you usually within 1 to 10 business day most likely within the 1st 72 business hours. They will schedule a time to come do a inspection, which we ask you to contact us and share that information as this us a very crucial part to getting the right things documented to that adjuster with statements that would would contribute to the adjuster having to approve the documented damages t ok be restored Once the adjuster complete the inspection, he submits his estimate written on a computer system that we also use meaning neither of us set the price we are only entering apple for apples aka same like kind and value to be removed and replaced. price is bases off of you zipcode and month where and when the works were privided/ incurred . Leaving you the homeowner only responsible for your deductible. Was you receive your estimate we will go over all approves line items with you and schedule them with you to meat you time line of what you have going on in your life. we can cater to all needs. We are financially set to do the works as fast as you would like or hold off until a certain time. That doing said through this entire process we do not request any down payments amd will be able to take the financial risks of completing the works 1st so you are never in a position to where yo iij have paid any moneys wiring about what the work will look like or when it will get done. Once we have finished all approved scope of works. We send off to them the final invoice stating all works have been completed and they release the rest of the funds allowed for those works. we are a 1 stop shop that will handle a those types of repairs. From roofing siding fascia soffit aluminum wraps garage doors drywall repair and painting amd more.

Target Market(s)

Home Owners, Useually 25 years old at least to 80 year olds. Most will be 30-50

Industry/Entity Type

Construction

Colors

Designer to choose colors to be used in the design.

Requirements
Must have
• My Company Name, My Logo that you can find On my Pixgram or web site fd- Gable Crest Renovations Inc. www.gablecrestrenovating.example
• My Slogan
• Where Tradesmen Turn Champions
• Contact info phone (555)263-7041
Nice to have
• Hail, and wind images Beautiful homes, disasters. Lightning striking hail falling SEVERE wind. I LOVE COMEDY. so any thing that is catchy or funny. Like Not a Shingle Mistake. as are number 1 thing we do is R&R Roofing
Should not have
• My Name,

```html
<!DOCTYPE html>
<html lang="en">
<head>
<meta charset="utf-8">
<title>Gable Crest Renovations Flyer</title>
<link href="https://fonts.googleapis.com/css2?family=Oswald:wght@600;700&family=Open+Sans:wght@400;700&family=Cinzel:wght@600&display=swap" rel="stylesheet">
<style>
:root{
  --maroon:#5a0a1e;
  --maroon-deep:#43071a;
  --ink:#2a1a1e;
  --white:#ffffff;
  --rule:#c9a8b0;
  --seal:#e9e9ee;
  --bg:#2b2b2b;
}
*{box-sizing:border-box;margin:0;padding:0}
html,body{width:1200px;height:800px;overflow:hidden;background:var(--bg)}
.flyer{position:absolute;left:307px;top:20px;width:586px;height:760px;background:var(--white);overflow:hidden;font-family:"Open Sans",Arial,sans-serif;color:var(--ink)}
.hero-photo{position:absolute;left:0;top:0;width:586px;height:312px;background:linear-gradient(115deg,#2f4fa8 0%,#3f63c4 35%,#9a7b3a 58%,#d99a38 75%,#e8b058 100%)}
.title-block{position:absolute;left:0;top:264px;width:332px;height:151px;background:var(--maroon);border-top-right-radius:18px;color:var(--white);padding:26px 0 0 30px}
.title-block .name{font-family:"Oswald",Arial,sans-serif;font-weight:700;font-size:36px;line-height:40px;letter-spacing:.5px;white-space:nowrap}
.title-block .name-wide{font-family:"Oswald",Arial,sans-serif;font-weight:700;font-size:34px;line-height:38px;letter-spacing:8px;white-space:nowrap}
.title-block .tagline{font-size:11.5px;margin-top:8px;letter-spacing:.2px;white-space:nowrap}
.badge-circle{position:absolute;left:337px;top:99px;width:240px;height:240px;border-radius:50%;background:var(--white);box-shadow:inset 0 0 0 4px #6d6d6d,inset 0 0 0 7px #fff;display:flex;align-items:center;justify-content:center;text-align:center}
.badge-circle .brand{font-weight:700;font-size:17px;line-height:22px;color:var(--maroon);width:150px}
.advantages{position:absolute;left:335px;top:312px;width:251px;height:103px;background:var(--white);border-left:2px solid var(--maroon)}
.bar{background:var(--maroon-deep);color:var(--white);margin:4px 4px 0 4px}
.advantages .bar{height:24px;font-size:11px;line-height:24px;padding-left:12px;letter-spacing:.3px;white-space:nowrap}
.advantages .bar b{font-weight:700}
.advantages p{font-size:10.3px;line-height:12.6px;padding:7px 8px 0 8px}
.about{position:absolute;left:0;top:415px;width:332px;height:266px;padding:18px 14px 0 18px;border-top:2px solid var(--maroon)}
.about h2,.services h2{font-weight:400;letter-spacing:3px}
.about h2{font-size:15px;color:var(--maroon);margin-bottom:8px}
.about p{font-size:10.3px;line-height:12.6px;margin-bottom:12px}
.services{position:absolute;left:335px;top:415px;width:251px;height:266px;border-left:2px solid var(--maroon);border-top:2px solid var(--maroon)}
.services .bar{height:27px;font-size:15px;line-height:27px;padding-left:8px;letter-spacing:3px}
.services ul{list-style:none;padding:10px 0 0 16px}
.services li{display:flex;align-items:center;height:36px;font-size:10.7px}
.services svg{width:26px;height:26px;margin-right:12px;flex:none}
.footer{position:absolute;left:0;top:681px;width:586px;height:79px;background:var(--maroon);color:var(--white)}
.footer .more{position:absolute;left:60px;top:9px;width:320px;text-align:center;font-size:12px;padding-bottom:6px;border-bottom:1px solid var(--rule)}
.footer .more b{font-weight:700}
.footer .contact{position:absolute;left:16px;top:45px;width:450px;display:flex;align-items:center;white-space:nowrap}
.footer .contact svg{width:14px;height:14px;margin-right:9px;flex:none}
.footer .phone{font-size:11px;letter-spacing:2px}
.footer .web{font-size:9.5px;letter-spacing:1.2px}
.footer .divider{width:1px;height:18px;background:var(--rule);margin:0 12px;flex:none}
.footer .creds{position:absolute;left:478px;top:6px;width:100px;height:70px;border-left:1px solid var(--rule);padding-left:12px}
.footer .creds .lbi{font-family:"Cinzel",serif;font-weight:600;font-size:8.5px;line-height:11px;letter-spacing:.6px}
.footer .seal{position:absolute;left:68px;top:3px;width:18px;height:24px;background:var(--seal);border-radius:2px}
.footer .social{display:flex;align-items:center;margin-top:8px;font-size:10px;font-weight:700}
.footer .social .sq{width:12px;height:12px;background:var(--white);margin-right:5px}
</style>
</head>
<body>
<main class="flyer">
  <div class="hero-photo" role="img" aria-label="Photo of a roofer in hard hat and safety vest laying shingles on a roof"></div>

  <div class="badge-circle">
    <div class="brand">Gable Crest Renovations Inc.</div>
  </div>

  <header class="title-block">
    <div class="name">GABLE CREST'S</div>
    <div class="name-wide">REMODELING</div>
    <div class="tagline">WHERE TRADESMEN TURN CHAMPIONS</div>
  </header>

  <section class="advantages">
    <div class="bar">OUR ADVANTAGES <b>WHY CHOOSE US</b></div>
    <p>At GCR, we constantly take advantage of the vast amount of available roofing industry training, and we provide our clients with the best client experience, and the highest quality and most efficient roofing systems.</p>
  </section>

  <section class="about">
    <h2>ABOUT US</h2>
    <p>Gable Crest Renovations is your one-stop shop for all your storm damage restoration needs. Our seasoned professionals use time-tested processes to restore your home after a storm, eliminating the hassles and headaches of working with multiple companies. Whether you need a roof replaced, or need exterior/interior damage repaired, you can trust Gable Crest Renovations to complete your projects.</p>
    <p>We have learned over the years what our clients want. While each client and their project has its own unique attributes, the overall desire of each seem to be same... Excellence. So that's what we provide! From the initial visit to final inspection and all the details in between. We have worked diligently to ensure that our team and implemented systems are living up to that standard!</p>
  </section>

  <section class="services">
    <h2 class="bar">OUR SERVICES</h2>
    <ul>
      <li><svg viewBox="0 0 26 26"><circle cx="13" cy="13" r="13" fill="#43071a"/><path d="M5 17 L13 8 L21 17 Z" fill="#fff"/></svg>Residential Roofing</li>
      <li><svg viewBox="0 0 26 26"><circle cx="13" cy="13" r="13" fill="#43071a"/><path d="M6 18 L10 8 H20 L17 18 Z" fill="#fff"/><path d="M11 18 L14 9 M14 18 L17 9" stroke="#43071a" stroke-width="1.2"/></svg>Commercial Roofing</li>
      <li><svg viewBox="0 0 26 26"><circle cx="13" cy="13" r="13" fill="#43071a"/><path d="M6 13 L13 6 L20 13 V20 H6 Z" fill="#fff"/><rect x="11" y="14" width="4" height="6" fill="#43071a"/></svg>Residential Exterior</li>
      <li><svg viewBox="0 0 26 26"><circle cx="13" cy="13" r="13" fill="#43071a"/><path d="M7 8 L18 19" stroke="#fff" stroke-width="3" stroke-linecap="round"/><path d="M16 7 a3 3 0 1 0 3 3" stroke="#fff" stroke-width="2" fill="none"/></svg>Roof leak repair</li>
      <li><svg viewBox="0 0 26 26"><circle cx="13" cy="13" r="13" fill="#43071a"/><path d="M7 7 L19 19 M19 7 L7 19" stroke="#fff" stroke-width="2.6" stroke-linecap="round"/></svg>Roof Maintenance</li>
      <li><svg viewBox="0 0 26 26"><circle cx="13" cy="13" r="13" fill="#43071a"/><path d="M8 18 L18 8" stroke="#fff" stroke-width="3" stroke-linecap="round"/><path d="M8 8 L12 12" stroke="#fff" stroke-width="2" stroke-linecap="round"/></svg>Specialty Roofing</li>
    </ul>
  </section>

  <footer class="footer">
    <div class="more">For More Information <b>CONTACT US</b></div>
    <div class="contact">
      <svg viewBox="0 0 14 14"><path d="M2 5 Q7 1 12 5 L11 7 L9 6 V5 H5 V6 L3 7 Z M3 8 H11 V12 H3 Z" fill="#fff"/></svg>
      <span class="phone">(555)263-7041</span>
      <span class="divider"></span>
      <svg viewBox="0 0 14 14"><circle cx="7" cy="7" r="6" fill="none" stroke="#fff"/><path d="M1 7 H13 M7 1 V13" stroke="#fff" stroke-width=".8"/><ellipse cx="7" cy="7" rx="3" ry="6" fill="none" stroke="#fff" stroke-width=".8"/></svg>
      <span class="web">WWW.GABLECRESTRENOVATING.EXAMPLE</span>
    </div>
    <div class="creds">
      <div class="lbi">LICENSED<br>BONDED<br>INSURED</div>
      <div class="seal"></div>
      <div class="social"><span class="sq"></span>Pixgram</div>
    </div>
  </footer>
</main>
</body>
</html>
```